Saving Lives with Dental Sleep Medicine

Looking for a brochure to market Dental Sleep Medicine educational courses . Whoever wins this bid will be hired to design the rest of our marketing campaign.
Design should be clean, simple with a modern feel. Not busy. Our courses utilize the most modern technology available.
Brochure content is attached, if you can't fit it all that is ok, we can tweak the content later. We are more focused on the look and feel of this design.
This brochure is marketing a 2 day course so there needs to be a spot for date, location, time & cost. As well as a notice of where to register VelmoraLearning.com, info@velmoralearning.com or call 1.800.###.#### and registration fees.
Also need a spot for Dr. Pelloquist's bio (attached). It's too long so just leave as much space as you can and we can amend the content.
Thank you so much. Looking forward to your designs. VelmEd Team :-)
Updates
Hello,
We are hoping for a minimalist design. Not busy. Clean and simple. We can reduce and minimize verbiage as needed. Just looking for layout and design.
Target Market(s)
Dentists
Requirements
Must have
- Clean lines, simple feel, minimalist and modern. Same font as logo. Black, white, gray.
Should not have
- Busy look and feel

```html
<!DOCTYPE html>
<html lang="en">
<head>
<meta charset="utf-8">
<title>Sleep &amp; Airway Management Brochure</title>
<link rel="stylesheet" href="https://fonts.googleapis.com/css2?family=Montserrat:wght@600;700&family=Quicksand:wght@400;500;700&display=swap">
<style>
:root{
  --ink:#2e2e36;
  --slate:#35353f;
  --slate-2:#42424c;
  --mist:#e4e4e8;
  --paper:#ffffff;
  --soft:#d9d9de;
  --muted:#bfbfc6;
  --tick:#3aa66a;
  --accent:#c9474f;
}
*{box-sizing:border-box;margin:0;padding:0}
html,body{width:1200px;height:810px;overflow:hidden;background:var(--paper)}
body{font-family:"Quicksand",sans-serif;color:var(--ink);position:relative}
.sheet{position:absolute;left:351px;width:501px;height:353px;display:flex;box-shadow:0 8px 10px -6px rgba(0,0,0,.25)}
.sheet--outside{top:25px}
.sheet--inside{top:433px}
.panel{position:relative;width:167px;height:353px;overflow:hidden}

/* photo placeholders */
.photo{position:absolute;display:block}

/* outside: bio */
.panel--bio{background:var(--slate)}
.panel--bio .photo{left:0;top:0;width:167px;height:110px;background:linear-gradient(135deg,#8a8a8a,#3b3b3b 60%,#d2d2d2)}
.bio{position:absolute;left:17px;top:124px;width:134px;color:#e2e2e6;font-size:6.3px;line-height:7.85px;text-align:justify;hyphens:auto}
.bio__name{font-weight:700;font-size:9.5px;color:#fff}

/* outside: contact */
.panel--contact{background:linear-gradient(90deg,#f4f4f6,#cfcfd4)}
.panel--contact .photo{left:0;top:0;width:167px;height:190px;background:linear-gradient(160deg,#c9c9cf,#5b5b63 55%,#3a3a42)}
.band{position:absolute;left:0;top:190px;width:167px;height:35px;background:var(--slate);display:flex;align-items:center;padding-left:16px}
.brand{display:flex;align-items:center;gap:5px;font-family:"Quicksand",sans-serif;font-weight:500;color:#d8d8dc;white-space:nowrap}
.brand__mark{width:9px;height:9px;background:var(--accent)}
.band .brand{font-size:15px}
.contact__title{position:absolute;left:0;width:167px;top:234px;text-align:center;font-family:"Montserrat",sans-serif;font-weight:700;font-size:14px;color:var(--ink)}
.contact__phone{position:absolute;left:12px;top:255px;width:142px;height:20px;border-radius:10px;background:var(--slate);color:#fff;font-family:"Montserrat",sans-serif;font-weight:600;font-size:10.5px;display:flex;align-items:center;justify-content:center;gap:5px}
.contact__line{position:absolute;left:17px;font-size:8.2px;display:flex;align-items:center;gap:4px;color:var(--ink);white-space:nowrap}
.contact__line--mail{top:279px}
.contact__line--web{top:292px}
.social{position:absolute;top:309px;width:20px;height:20px;border-radius:50%;background:var(--slate)}
.social--a{left:52px}
.social--b{left:89px}

/* outside: cover */
.panel--cover{background:linear-gradient(180deg,#4b4b55,#2f2f38)}
.panel--cover .photo--room{left:0;top:37px;width:167px;height:178px;background:linear-gradient(160deg,#8b7a70,#4f4f59 50%,#383842)}
.cover__band{position:absolute;left:0;top:0;width:167px;height:37px;background:var(--slate-2);display:flex;align-items:center;justify-content:center}
.cover__band .brand{font-size:15.5px}
.cover__title{position:absolute;left:17px;top:88px;font-family:"Montserrat",sans-serif;font-weight:700;color:#e6e6ea;line-height:1.12}
.cover__title span{display:block}
.t1{font-size:14.5px}.t2{font-size:17.5px}.t3{font-size:12.6px}
.cover__sub{position:absolute;left:18px;top:190px;font-family:"Montserrat",sans-serif;font-weight:700;font-size:10.6px;line-height:15px;color:#fff}
.photo--presenter{left:-48px;top:212px;width:70px;height:141px;background:linear-gradient(180deg,#6f6f7a,#2d3152);border-radius:30px 30px 0 0;z-index:2}
.details{position:absolute;left:21px;top:229px;width:135px;height:87px;background:rgba(255,255,255,.08);padding:5px 12px;font-size:8px;line-height:16px;color:#e3e3e8}
.details__site{font-size:6.5px;margin-left:10px}
.cover__doctor{position:absolute;left:27px;top:322px;font-size:14px;color:#f0f0f3}

/* inside */
.panel--inside{background:linear-gradient(90deg,#e6e6ea,#d3d3d8)}
.panel--inside.panel--white{background:var(--paper)}
.inside__top{position:absolute;left:0;top:0;width:167px;height:115px;background:var(--slate)}
.panel--inside .photo{left:17px;top:28px;width:131px;height:86px}
.photo--lab{background:linear-gradient(135deg,#7d7d80,#b8b0a8 45%,#4c4c54)}
.photo--screen{background:linear-gradient(120deg,#c6b5a6,#eaeaf0 50%,#4a6a8c)}
.photo--group{background:linear-gradient(135deg,#9a7a66,#d0d0d4 50%,#7a2a2a)}
.inside__head{position:absolute;left:0;width:167px;top:135px;text-align:center;font-family:"Montserrat",sans-serif;font-weight:600;font-size:6.4px;letter-spacing:.1px;color:var(--ink)}
.inside__rule{position:absolute;left:71px;top:152px;width:25px;height:1px;background:var(--ink)}
.inside__text{position:absolute;left:17px;top:164px;width:133px;font-size:6.5px;line-height:7.85px;text-align:justify;color:#3a3a42}
.topics li{list-style:none}
.topics li::before{content:"• "}
.desc p+p{margin-top:7.8px}
.goals li{list-style:none;margin-bottom:0}
.tick{display:inline-block;width:7px;height:7px;vertical-align:-1px;margin:0 5px 0 5px}
</style>
</head>
<body>

<section class="sheet sheet--outside">
  <article class="panel panel--bio">
    <div class="photo" role="img" aria-label="Black and white portrait of Dr. Pelloquist in a suit"></div>
    <p class="bio"><span class="bio__name">Dr. Pelloquist</span> received his Doctor of Dental Surgery (DDS) Degree and Bachelor of Medical Sciences from Northfield University. He also earned fellowships from International Society of Facial Aesthetics &amp; Summit Institute for Advanced Dental Studies. He then furthered his education and training by completing a Research Fellowship in the area of “Sleep and Dental Sleep Medicine” at Harlow University Hospital (HUH), in Harlow, Wessland.<br>Dr. Pelloquist is a general dentist who maintains a group of private practices in Eastvale and Ridgeport with an interest in Dental Sleep Medicine and TMD Management. He is actively involved in clinical research in Dental Sleep Medicine and his research focuses on developing new technologies to improve treatment outcome predictability and patient selection in Oral Appliance Therapy for patients with OSA (i.e. Obstructive Sleep Apnea) and improving clinical workflow efficiencies, utilizing different digital technologies.</p>
  </article>

  <article class="panel panel--contact">
    <div class="photo" role="img" aria-label="Course attendees seated around a conference table with laptops"></div>
    <div class="band"><span class="brand"><span class="brand__mark"></span>VelmoraLearning</span></div>
    <h2 class="contact__title">CONTACT</h2>
    <div class="contact__phone">
      <svg width="8" height="8" viewBox="0 0 24 24"><path fill="#fff" d="M6.6 10.8a15 15 0 0 0 6.6 6.6l2.2-2.2a1 1 0 0 1 1-.25 11.4 11.4 0 0 0 3.6.57 1 1 0 0 1 1 1V20a1 1 0 0 1-1 1A17 17 0 0 1 3 4a1 1 0 0 1 1-1h3.5a1 1 0 0 1 1 1c0 1.25.2 2.45.57 3.57a1 1 0 0 1-.25 1z"/></svg>
      1.800.000.0000
    </div>
    <div class="contact__line contact__line--mail">
      <svg width="7" height="5" viewBox="0 0 14 10"><rect x=".5" y=".5" width="13" height="9" fill="none" stroke="#555" /><path d="M.5.5 7 6l6.5-5.5" fill="none" stroke="#555"/></svg>
      info@velmoralearning.com
    </div>
    <div class="contact__line contact__line--web">
      <svg width="7" height="7" viewBox="0 0 14 14"><circle cx="7" cy="7" r="6" fill="none" stroke="#555"/><path d="M1 7h12M7 1c-3 3-3 9 0 12M7 1c3 3 3 9 0 12" fill="none" stroke="#555"/></svg>
      &nbsp;VelmoraLearning.com
    </div>
    <span class="social social--a" aria-hidden="true"></span>
    <span class="social social--b" aria-hidden="true"></span>
  </article>

  <article class="panel panel--cover">
    <div class="cover__band"><span class="brand"><span class="brand__mark"></span>VelmoraLearning</span></div>
    <div class="photo photo--room" role="img" aria-label="Lecture room with attendees at laptops"></div>
    <h1 class="cover__title"><span class="t1">SLEEP &amp; AIRWAY</span><span class="t2">MANAGEMENT</span><span class="t3">IN A DENTAL CLINIC</span></h1>
    <p class="cover__sub">SomnaFit Plus System &amp; Fully<br>Digital Workflows for OAT</p>
    <div class="photo photo--presenter" role="img" aria-label="Presenter in a navy suit holding a remote"></div>
    <div class="details">
      Date:<br>Time:<br>Location:<br>Register:<span class="details__site">VelmoraLearning.com</span><br>Registration fees:
    </div>
    <p class="cover__doctor">Dr. Pelloquist</p>
  </article>
</section>

<section class="sheet sheet--inside">
  <article class="panel panel--inside">
    <div class="inside__top"></div>
    <div class="photo photo--lab" role="img" aria-label="Attendees gathered around a dental chair in a clinic"></div>
    <h3 class="inside__head">TOPICS COVERED</h3>
    <span class="inside__rule"></span>
    <ul class="inside__text topics">
      <li>Fundamentals of Sleep &amp; Sleep Disorders</li>
      <li>Understand Obstructive Sleep Apnea (OSA) &amp; Treatment Options</li>
      <li>How to Implement an effective Sleep Screening Protocol in a Dental Clinic</li>
      <li>Sleep Testing</li>
      <li>How to order an appliance for OAT</li>
      <li>Appliance Selection</li>
      <li>Importance of patient selection</li>
      <li>Overview of SomnaFit Plus System</li>
      <li>Hands-on workshop for SomnaFit Tray Fitting</li>
      <li>Hands-on workshop for Bite-Registration</li>
      <li>Technology &amp; Sleep</li>
      <li>Fully Digital Workflow for OAT</li>
      <li>SomnaFit Plus Case Studies</li>
      <li>Medical Billing for OAT</li>
      <li>How to maximize the utilization of your SomnaFit Plus at your clinic</li>
      <li>Simple and easy to follow clinical workflow</li>
    </ul>
  </article>

  <article class="panel panel--inside panel--white">
    <div class="inside__top"></div>
    <div class="photo photo--screen" role="img" aria-label="Clinician viewing a digital dental scan on a monitor"></div>
    <h3 class="inside__head">COURSE DESCRIPTION</h3>
    <span class="inside__rule"></span>
    <div class="inside__text desc">
      <p>Dental Sleep Medicine (DSM) has been growing rapidly over the past decade. Despite such growth, Oral Appliance Therapy (OAT) could be challenging in terms of predictability and workflow efficiency, resulting in many clinicians being reluctant to incorporate “Sleep &amp; OAT” into their clinics. However, most of these challenges can now be addressed by utilizing available technologies in healthcare industry; resulting in improved and predictable clinical workflows, patient experience, quality of care and access to care.</p>
      <p>This program will review the importance of Sleep &amp; Airway Management in comprehensive inter-disciplinary treatment planning and how airway &amp; sleep disorders, if left untreated, could adversely impact the long-term prognosis of dental treatments.</p>
    </div>
  </article>

  <article class="panel panel--inside">
    <div class="inside__top"></div>
    <div class="photo photo--group" role="img" aria-label="Instructor speaking to a group of attendees in a clinic"></div>
    <h3 class="inside__head">LEARNING OBJECTIVES</h3>
    <span class="inside__rule"></span>
    <ul class="inside__text goals">
      <li><svg class="tick" viewBox="0 0 14 14"><circle cx="7" cy="7" r="6" fill="none" stroke="var(--tick)" stroke-width="1.3"/><path d="M4 7.2l2 2 4-4.2" fill="none" stroke="var(--tick)" stroke-width="1.3"/></svg>Step by step instruction on how to systematically integrate sleep into your practice</li>
      <li><svg class="tick" viewBox="0 0 14 14"><circle cx="7" cy="7" r="6" fill="none" stroke="var(--tick)" stroke-width="1.3"/><path d="M4 7.2l2 2 4-4.2" fill="none" stroke="var(--tick)" stroke-width="1.3"/></svg>Why dental clinics should have a comprehensive understanding of sleep &amp; airway disorders, and educate their patients</li>
      <li><svg class="tick" viewBox="0 0 14 14"><circle cx="7" cy="7" r="6" fill="none" stroke="var(--tick)" stroke-width="1.3"/><path d="M4 7.2l2 2 4-4.2" fill="none" stroke="var(--tick)" stroke-width="1.3"/></svg>How to implement a sleep and airway management program in a dental clinic</li>
      <li><svg class="tick" viewBox="0 0 14 14"><circle cx="7" cy="7" r="6" fill="none" stroke="var(--tick)" stroke-width="1.3"/><path d="M4 7.2l2 2 4-4.2" fill="none" stroke="var(--tick)" stroke-width="1.3"/></svg>Overview of some of the latest technologies in dentistry and how each could be utilized in Dental Sleep Medicine (DSM)</li>
      <li><svg class="tick" viewBox="0 0 14 14"><circle cx="7" cy="7" r="6" fill="none" stroke="var(--tick)" stroke-width="1.3"/><path d="M4 7.2l2 2 4-4.2" fill="none" stroke="var(--tick)" stroke-width="1.3"/></svg>How to utilize your SomnaFit Plus System effectively in your clinic</li>
      <li><svg class="tick" viewBox="0 0 14 14"><circle cx="7" cy="7" r="6" fill="none" stroke="var(--tick)" stroke-width="1.3"/><path d="M4 7.2l2 2 4-4.2" fill="none" stroke="var(--tick)" stroke-width="1.3"/></svg>Proper selection of oral appliances for OSA</li>
      <li><svg class="tick" viewBox="0 0 14 14"><circle cx="7" cy="7" r="6" fill="none" stroke="var(--tick)" stroke-width="1.3"/><path d="M4 7.2l2 2 4-4.2" fill="none" stroke="var(--tick)" stroke-width="1.3"/></svg>Medical Billing for OAT</li>
    </ul>
  </article>
</section>

</body>
</html>
```